Bref créative
Sun Path & Oak Hill
Business Cards & Stationary
Use same font as used in my logo
marla teswick
director of operations
p o box 87
gravette, ar 72915
spoh@postvale.com
501(c)3

```html
<!DOCTYPE html>
<html lang="en">
<head>
<meta charset="utf-8">
<title>Sun Path &amp; Oak Hill — Letterhead</title>
<link rel="stylesheet" href="https://fonts.googleapis.com/css2?family=Caveat:wght@500&family=Montserrat:wght@400;700&display=swap">
<style>
  :root {
    --page-bg: #ffffff;
    --sheet-bg: #ffffff;
    --sheet-edge: #d9d9d9;
    --ink: #2b2b2b;
    --ink-soft: #6e6e6e;
    --blush: #f3bfd1;
    --blush-deep: #e58fae;
    --stone: #a6a6a6;
    --stone-deep: #6f6f6f;
    --band-dark: #6a6a6a;
  }
  * { box-sizing: border-box; margin: 0; padding: 0; }
  html, body { width: 1200px; height: 941px; overflow: hidden; background: var(--page-bg); }
  .board { position: relative; width: 1200px; height: 941px; font-family: "Montserrat", Arial, sans-serif; color: var(--ink); }

  .board-title {
    position: absolute; left: 738px; top: 98px;
    font-weight: 700; font-size: 26px; letter-spacing: 0.5px; color: #111;
  }

  .sheet {
    position: absolute; width: 470px; height: 678px;
    background: var(--sheet-bg);
    border: 1px solid var(--sheet-edge);
    box-shadow: 1px 1px 4px rgba(0,0,0,0.12);
  }
  .sheet--blush { left: 91px; top: 99px; }
  .sheet--stone { left: 626px; top: 216px; }

  .brand { position: absolute; left: 12px; top: 10px; display: flex; align-items: center; gap: 8px; }
  .brand-dot { width: 32px; height: 32px; border-radius: 50%; }
  .sheet--blush .brand-dot { background: var(--blush); }
  .sheet--stone .brand-dot { background: var(--stone); }
  .brand-name { font-family: "Caveat", cursive; font-weight: 500; font-size: 22px; line-height: 0.95; color: var(--ink); }

  .brand-line { position: absolute; left: 28px; top: 74px; font-size: 7.5px; letter-spacing: 2.2px; text-transform: uppercase; }
  .sheet--blush .brand-line { color: var(--blush-deep); }
  .sheet--stone .brand-line { color: var(--stone-deep); }
  .brand-status { position: absolute; left: 28px; top: 85px; font-size: 5px; color: var(--ink-soft); }

  .sender { position: absolute; left: 28px; top: 96px; }
  .sender-name { font-family: "Caveat", cursive; font-weight: 500; font-size: 14px; color: var(--blush-deep); line-height: 1; }
  .sender-role { font-size: 5px; letter-spacing: 0.5px; color: var(--ink-soft); text-transform: uppercase; margin-top: 2px; }

  .mission { position: absolute; right: 8px; bottom: 26px; width: 122px; height: 122px; }
  .mission-disc { position: absolute; inset: 0; border-radius: 50%; }
  .sheet--blush .mission-disc { background: var(--blush); }
  .sheet--stone .mission-disc { background: var(--stone); }
  .mission-text {
    position: absolute; left: 16px; right: 6px; top: 40px;
    font-family: "Caveat", cursive; font-weight: 500; font-size: 18px; line-height: 1.05; color: var(--ink);
  }

  .contact {
    position: absolute; left: 0; right: 150px; bottom: 14px; text-align: center;
    font-size: 6px; color: var(--ink-soft); letter-spacing: 0.2px;
  }
  .band { position: absolute; left: 0; right: 0; bottom: 0; height: 7px; }
  .sheet--blush .band { background: var(--blush); }
  .sheet--stone .band { background: var(--band-dark); }
</style>
</head>
<body>
<main class="board">
  <h1 class="board-title">LETTERHEAD</h1>

  <section class="sheet sheet--blush" aria-label="Letterhead, blush edition">
    <div class="brand"><span class="brand-dot"></span><span class="brand-name">Sun Path &amp;<br>Oak Hill</span></div>
    <p class="brand-line">Share with others</p>
    <p class="brand-status">a 501(c)3</p>
    <div class="sender">
      <p class="sender-name">marla teswick</p>
      <p class="sender-role">Director</p>
    </div>
    <div class="mission">
      <span class="mission-disc"></span>
      <p class="mission-text">providing food<br>for the hungry</p>
    </div>
    <p class="contact">701.555.0148 &nbsp;|&nbsp; spoh@postvale.com &nbsp;|&nbsp; PO Box 87 Fernbrook, ND 58910</p>
    <div class="band"></div>
  </section>

  <section class="sheet sheet--stone" aria-label="Letterhead, stone edition">
    <div class="brand"><span class="brand-dot"></span><span class="brand-name">Sun Path &amp;<br>Oak Hill</span></div>
    <p class="brand-line">Share with others</p>
    <p class="brand-status">a 501(c)3</p>
    <div class="sender">
      <p class="sender-name">marla teswick</p>
      <p class="sender-role">Director</p>
    </div>
    <div class="mission">
      <span class="mission-disc"></span>
      <p class="mission-text">providing food<br>for the hungry</p>
    </div>
    <p class="contact">701.555.0148 &nbsp;|&nbsp; spoh@postvale.com &nbsp;|&nbsp; PO Box 87 Fernbrook, ND 58910</p>
    <div class="band"></div>
  </section>
</main>
</body>
</html>
```